Personal coach needs brochure design for inspirational essay about authenticity

Overview:
I want a beautiful brochure, 11”x17” that folds to 8-1/2”x11” with 4 pages. Think of it as an oversize greeting card.
• Front cover: photograph of a dancer and title with attribution of quote (Pixavanto jpeg photo attached)
• Inside spread: Copy (Edith Sorrel copy attached) with some appropriate illustration, based on cover photo
• Back cover: contact information, brief descriptive copy, two small photos (jpeg photo attached; see copy for direction)
Copy for front cover title, inside spread and back cover is attached in doc titled "Edith Sorrel copy"

Purpose of brochure:
I'm a personal coach and once a year I produce a 4-page illustrated inspirational essay, which invites personal reflection on living a more mindful, meaningful life. Most people I send them to collect them. Someday in the future I'd like to put a collection of these essays into a coffee table book and also create a website for the collection, which is related to the personal coaching that I do.
I have the brochures printed hard copy. I have attached a few examples from previous years. Each has a unique design related to its theme.

Concept:
This year’s essay theme, “There will only ever be one you!” is based on a quote by Edith Sorrel, a famous modern dancer. The complete quote, which appears in the copy, is about being true to one’s authentic self. The essay is not about dance, but because the author of the quote was a dancer who personified this theme of being unique to self, I have selected a photo of dance for the cover.

Design Guidance:
Front cover: One possibility is to expand the background color of the Pixavanto photo so the photo seems to emerge from the background. But I am open to ideas. I think the photo is artsy enough as it is, but there may be other ways to treat it (e.g. special effects) that would also work. The title should appear somewhere. Make the attribution (--Edith Sorrel) in smaller type than the title.

Inside Spread: There may be ways to borrow a design motif from the cover photo to make the inside spread more visually interesting, i.e., not just straight copy. I think it may be helpful to make the font size of the quote larger than the rest of the copy, but it has to be read in sequence. Or maybe it's printed in same size as copy, but then also repeated and displayed by itself in larger type.

Back cover: If you look at some of the other examples I’ve sent, you’ll see how the back cover is typically handled. I want a reduced version of the cover to be placed near the line that says "this is the 16th in a series.." Then, there’s a jpeg photo of Edith Sorrel that should be placed next to the copy description of her.

Need extra days to review

```html
<!DOCTYPE html>
<html lang="en">
<head>
<meta charset="utf-8">
<title>There Will Only Ever Be One You – Brochure</title>
<link rel="stylesheet" href="https://fonts.googleapis.com/css2?family=Montserrat:ital,wght@0,400;0,500;0,700;1,500&family=Cormorant+Garamond:ital,wght@0,500;1,500&display=swap">
<style>
  :root {
    --backdrop: #e6e1d8;
    --paper: #fbeccb;
    --ink: #1f1d1a;
    --frame-grey: #a7abb3;
    --cover-dark: #1c1c1d;
    --cover-mid: #4a4c4f;
    --frame-white: #ffffff;
    --wall-grey: #8c9597;
  }
  * { margin: 0; padding: 0; box-sizing: border-box; }
  html, body { width: 1200px; height: 1200px; overflow: hidden; background: var(--backdrop); }
  .canvas { position: relative; width: 1200px; height: 1200px; overflow: hidden; }
  .spread { position: absolute; left: 175px; width: 850px; height: 550px; display: flex; box-shadow: 0 2px 10px rgba(0,0,0,.18); }
  .spread--outer { top: 35px; }
  .spread--inner { top: 615px; }
  .page { position: relative; width: 425px; height: 550px; background: var(--paper); color: var(--ink); font-family: "Montserrat", sans-serif; overflow: hidden; }

  /* Back cover */
  .back-cover__content { position: absolute; left: 50px; top: 42px; width: 324px; font-size: 7.3px; line-height: 10px; }
  .series-line { margin-bottom: 4px; }
  .series-line strong { font-weight: 500; }
  .contact { margin-bottom: 10px; }
  .contact b { font-weight: 700; }
  .copyright { margin-bottom: 6px; }
  .portrait { width: 148px; height: 129px; background: radial-gradient(ellipse at 55% 60%, #8a857d 0%, #2a2a2e 45%, #141418 100%); margin-bottom: 10px; }
  .portrait-caption { font-style: italic; font-weight: 500; margin-bottom: 16px; }
  .bio { text-align: justify; margin-bottom: 14px; }
  .bio b { font-weight: 700; }

  /* Front cover */
  .front-cover { background: radial-gradient(ellipse at 60% 40%, var(--cover-mid) 0%, #2c2d2f 55%, var(--cover-dark) 100%); }
  .front-cover__photo { position: absolute; inset: 0; background: radial-gradient(ellipse at 62% 38%, rgba(110,115,125,.55) 0%, rgba(40,44,52,.2) 45%, transparent 70%); }
  .front-cover__frame { position: absolute; left: 50px; top: 52px; width: 324px; height: 447px; border: 2px solid var(--frame-white); }
  .front-cover__title { position: absolute; left: 0; right: 0; top: 423px; text-align: center; color: #f4f1ea; font-family: "Cormorant Garamond", serif; font-weight: 500; font-size: 22px; line-height: 25px; }
  .front-cover__title em { font-style: italic; font-size: 21px; letter-spacing: .5px; }

  /* Inside spread */
  .essay-frame { position: absolute; left: 52px; top: 51px; width: 323px; height: 447px; border: 2px solid var(--frame-grey); }
  .essay { position: absolute; left: 77px; top: 83px; width: 273px; font-size: 8.3px; line-height: 10.4px; text-align: justify; }
  .essay p { margin-bottom: 10.4px; }
  .dancer-photo { position: absolute; left: 0; top: 0; width: 425px; height: 243px; background: linear-gradient(135deg, #a7b0b1 0%, var(--wall-grey) 50%, #6b7476 100%); }
  .quote-frame { position: absolute; left: 50px; top: 51px; width: 323px; height: 447px; border: 2px solid var(--frame-white); border-top: none; }
  .quote-frame::before { content: ""; position: absolute; left: -2px; right: -2px; top: 0; height: 192px; border: 2px solid var(--frame-white); border-bottom: none; }
  .quote-frame::after { content: ""; position: absolute; left: -2px; right: -2px; top: 192px; bottom: -2px; border: 2px solid var(--frame-grey); border-top: none; }
  .pull-quote { position: absolute; left: 77px; top: 262px; width: 270px; text-align: center; font-size: 8.6px; line-height: 10.4px; font-weight: 500; }
  .reflection { position: absolute; left: 75px; top: 376px; width: 274px; font-size: 8.3px; line-height: 10.4px; text-align: justify; }
  .reflection p { margin-bottom: 10.4px; }
</style>
</head>
<body>
<div class="canvas">

  <section class="spread spread--outer">
    <article class="page back-cover">
      <div class="back-cover__content">
        <p class="series-line"><strong>There Will Only Ever Be One You</strong> is the 16th in a series of Labor Day essays inviting a moment of reflection on living a more meaningful, more mindful life</p>
        <p class="contact">Nora Vell Ashby, Ph.D.<br>Heron Hill House<br>18 Orchard Lane<br>Linden Falls, Vermont&nbsp; 05099</p>
        <p class="contact"><b>Mobile:</b>&nbsp; 555-014-2287<br><b>Email:</b> nvashby@mailwell.net</p>
        <p class="copyright">©2023</p>
        <div class="portrait" role="img" aria-label="Black and white photograph of Edith Sorrel dancing in a flowing white dress"></div>
        <p class="portrait-caption">“Edith Sorrel in Song to the<br>Valley, No. 1”© The Clara Wren</p>
        <p class="bio"><b>ABOUT EDITH SORREL:</b>&nbsp; Born in 1896, Edith Sorrel danced and taught for nearly 70 years.She is recognized as a primal artistic force of the 20th century, whose influence on modernity has been compared to Anton Velde, Conor Brask, Ilya Montrov, and Henry Lisle Oakes. Her themes dealt with the lives and conflicts of ordinary people, and she brought serious issues to the stage like war, poverty, intolerance and the injustices faced by workers &amp; the displaced. Rebelling against conventions of the past, her dancing &amp; choreography exposed the depths of human emotion through intense movements that were forceful, stark, angular, jagged, and percussive – startlingly unlike the formality of classical ballet, which she saw as antiquated.</p>
        <p class="bio"><b>About Photographer Clara Wren:</b> In 1938 Clara Wren saw a performance by modern dancer and choreographer Edith Sorrel. Wren was so inspired by the dance performance that she introduced herself to Sorrel, and the two artists began an artistic collaboration that lasted more than 50 years.Wren often photographed dancers in action, to capture the emotion behind their movement. Her artistic style was in line with Sorrel’s philosophy of dance. This photo from the dance, <i>“Song to the Valley,”</i> is one of Wren’s most famous photographs. The title of this work comes from a Lydia Marsh poem, which inspired Sorrel to create a dance performance based on Marsh’s life.</p>
      </div>
    </article>

    <article class="page front-cover">
      <div class="front-cover__photo" role="img" aria-label="Photograph of a leaping dancer in a dark flowing dress amid a cloud of grey dust"></div>
      <div class="front-cover__frame"></div>
      <h1 class="front-cover__title">There will only ever be one you!<br><em>– Edith&nbsp; Sorrel</em></h1>
    </article>
  </section>

  <section class="spread spread--inner">
    <article class="page essay-page">
      <div class="essay-frame"></div>
      <div class="essay">
        <p>In the rural Ohio village where I grew up, one of the highlights of Sunday morning church service -- in between congregational hymn-singing and the preacher’s sermon -- was the “special selection,” a musical performance by a parishioner. Typically, it was a vocalist or instrumental on piano, organ or violin.&nbsp; One Sunday, we were surprised by an unusual performance. A plump, buxom farm wife approached the pulpit, puckered up her lips and unexpectedly began to whistle the hymn “The Old Rugged Cross.” As a 10-year-old, I found this hilarious as I tried to choke back my wide-eyed amazement and giggles.</p>
        <p>Despite the irreverence of my pre-adolescent reaction, this memory has stayed with me for decades as an iconic example of the wonderment of individual differences. Of the delight I find in witnessing someone express herself in sometimes surprising and even courageous ways. Of the marvel of beholding a person be truly authentic and uniquely original.</p>
        <p>Someone who personified the irrepressible impulse to express her individuality was the early 20th century dancer and choreographer Edith Sorrel.&nbsp; A pioneer of modern dance, she&nbsp; threw tradition overboard and was inspired to dance in a way that was a radical departure from the formalized style and rigidly dictated forms of classical ballet. Sorrel felt compelled to express the rawness and emotion of human experience in her dancing -- not just present a form of pretty entertainment. Iconoclastically brilliant, she created a new language of dance, a revolutionary vocabulary of movement that electrified the stage, often creating a visceral response in the audience.</p>
        <p>In her biography of Sorrel, her friend and equally talented choreographer Ruth Calloway recalled that despite sensational reviews for her own innovative work in the Broadway musical Prairie Song!, Calloway had a gnawing feeling that her work was only mediocre.&nbsp; Calloway confessed her anxieties to Sorrel who listened quietly and then responded, “There will only ever be one you!” Continuing, she added:</p>
      </div>
    </article>

    <article class="page quote-page">
      <div class="dancer-photo" role="img" aria-label="Photograph of a ballerina in a black dress leaping in a split jump against a grey concrete wall"></div>
      <div class="quote-frame"></div>
      <p class="pull-quote">“There is a spark, a pulse, a current, a stirring that moves through you and becomes motion.&nbsp; And because no one else has ever been you, what you make of it is unlike anything else. And if you hold it back, it is lost to everyone. It is not your task to decide how fine it is, how much it is worth or how it measures against the work of others. It is your task to keep it your own, plainly and honestly, to keep the channel open. Stay open and alert to the impulses that stir you. Above all else, keep the channel open!”</p>
      <div class="reflection">
        <p>Sorrel’s wisdom reminds us that we must not hold back or judge our gifts. Although there may be moments when we doubt ourselves or when we worry that we’re not good enough, our job is to be fearless and to “keep the channel open.”</p>
        <p>Guard the precious miracle of your own uniqueness. Find that home-sweet-home feeling&nbsp; where you feel you are your most authentic self.&nbsp; There will only ever be one you!&nbsp; And importantly, respect the differences of others.&nbsp; Our world would be a drab, boring place if we all&nbsp; only whistled one tune.</p>
      </div>
    </article>
  </section>

</div>
</body>
</html>
```